After school program needs an end of the year flyer to ask for donations

We need a 6x9 flyer front and back that shows some pictures, has some copy and our contact information. We are a non-profit organization that does afterschool programs for at-risk children in Brookdale, CA. This is our end of the year appeal for our donors to help us finish the year strong! We want it to celebrate what we've done and invite people to participate with us.

Target Market(s)

Donors on mailing list

Industry/Entity Type

Non-Profit

Font styles to use
Serif

Requirements
Must have
• pictures, text, contact information, space for stamp, return address, and mailing address

```html
<!DOCTYPE html>
<html lang="en">
<head>
<meta charset="utf-8">
<title>Maplewood Family Learning Center – Year-End Appeal Postcard</title>
<link rel="stylesheet" href="https://fonts.googleapis.com/css2?family=Lato:ital,wght@0,400;0,700;0,900;1,400;1,700&display=swap">
<style>
:root{
  --blue:#4a74b9;
  --charcoal:#3a3a3c;
  --paper:#ffffff;
  --panel-grey:#e4e5e8;
  --ink:#1f1f1f;
  --line:#b9b9b9;
  --stage:#ececec;
  --photo-warm-a:#b0553c;
  --photo-warm-b:#4c5e7e;
  --photo-cool-a:#5a6f95;
  --photo-cool-b:#3a4a38;
}
*{box-sizing:border-box;margin:0;padding:0}
html,body{width:997px;height:1200px;overflow:hidden;background:var(--stage)}
body{position:relative;font-family:"Lato",Arial,sans-serif;color:var(--ink)}

.card{position:absolute;background:var(--paper);box-shadow:0 3px 10px rgba(0,0,0,.25);overflow:hidden}

/* ---------- front ---------- */
.front{left:113px;top:113px;width:728px;height:487px}
.front-header{position:absolute;left:0;top:0;width:100%;height:86px;background:var(--paper)}
.front-title{position:absolute;left:136px;top:34px;font-size:29px;font-weight:400;letter-spacing:.2px;color:var(--ink);white-space:nowrap}
.brand-tile{position:absolute;left:31px;top:13px;width:86px;height:106px;background:var(--paper);border:2px solid var(--blue);z-index:2;display:flex;flex-direction:column;align-items:center;justify-content:center;gap:6px;text-align:center}
.brand-tile .mark{width:22px;height:22px;background:var(--blue)}
.brand-tile .name{font-size:9px;font-weight:700;line-height:1.2;color:var(--ink)}
.front-photo{position:absolute;left:0;top:86px;width:100%;height:278px;background:linear-gradient(135deg,var(--photo-warm-a) 0%,#a4523e 40%,var(--photo-warm-b) 100%)}
.front-tagline{position:absolute;left:18px;top:381px;font-size:19px;line-height:29px;color:var(--ink)}
.donate-box{position:absolute;left:451px;top:378px;width:255px;height:67px;background:var(--blue);color:#fff;text-align:center;box-shadow:0 4px 5px rgba(0,0,0,.3);padding-top:6px}
.donate-box .small{font-size:12.5px;font-style:italic;line-height:16px}
.donate-box .url{font-size:20px;font-weight:900;letter-spacing:.5px;line-height:24px}
.front-footer{position:absolute;left:0;bottom:0;width:100%;height:32px;background:var(--charcoal);color:#fff;font-size:13px;font-style:italic;display:flex;align-items:center;justify-content:space-between;padding:0 12px 0 18px;white-space:nowrap}
.front-footer .social{display:flex;align-items:center;gap:10px}
.social-square{width:18px;height:18px;background:#fff}

/* ---------- back ---------- */
.back{left:205px;top:626px;width:731px;height:485px}
.appeal{position:absolute;left:0;top:0;width:439px;height:100%}
.appeal-header{position:absolute;left:0;top:0;width:100%;height:75px;background:var(--blue);color:#fff;font-size:25px;font-weight:400;padding:26px 0 0 18px;white-space:nowrap}
.appeal-photo{position:absolute;left:0;top:75px;width:429px;height:113px;background:linear-gradient(100deg,var(--photo-cool-a) 0%,#7b6a72 45%,var(--photo-cool-b) 100%)}
.appeal-body{position:absolute;left:0;top:188px;width:429px;height:205px;background:var(--panel-grey)}
.appeal-copy{position:absolute;left:30px;top:20px;width:378px;font-size:10.9px;line-height:15.1px;text-align:justify}
.appeal-cta{position:absolute;left:30px;top:134px;width:374px;height:48px;background:var(--charcoal);color:#fff;text-align:center;font-size:12px;line-height:18px;padding-top:5px;box-shadow:0 5px 5px rgba(0,0,0,.25);white-space:nowrap}
.appeal-cta b{font-size:15px;font-weight:900}
.appeal-footer{position:absolute;left:0;top:393px;width:100%;height:75px;background:var(--blue);color:#fff;font-size:16.5px;line-height:20.5px;padding:8px 0 0 26px;font-style:normal}
.appeal-footer .social-square{position:absolute;left:400px;top:35px;width:27px;height:27px;background:var(--charcoal)}

.mailing{position:absolute;left:439px;top:0;width:292px;height:100%}
.return-address{position:absolute;left:17px;top:32px;font-size:8px;line-height:10.3px;font-style:normal;color:#333}
.stamp-box{position:absolute;left:183px;top:31px;width:83px;height:64px;border:1px solid #999}
.address-lines{position:absolute;left:19px;top:164px;width:249px}
.address-lines span{display:block;height:31px;border-top:1px solid var(--line)}
.seal{position:absolute;left:111px;top:312px;width:76px;display:flex;flex-direction:column;align-items:center;gap:5px;text-align:center}
.seal .mark{width:20px;height:20px;background:var(--blue)}
.seal .name{font-size:8.5px;font-weight:700;line-height:1.2}
.legal{position:absolute;left:6px;top:415px;width:280px;text-align:center;font-size:8.2px;font-style:italic;font-weight:700;line-height:11.8px;white-space:nowrap}
.mailing-footer{position:absolute;left:0;bottom:0;width:100%;height:20px;background:var(--charcoal);color:#fff;font-size:15px;font-style:italic;letter-spacing:.8px;text-align:center;line-height:20px}
</style>
</head>
<body>

<section class="card front">
  <header class="front-header">
    <h1 class="front-title">MAPLEWOOD FAMILY LEARNING CENTER</h1>
  </header>
  <div class="brand-tile">
    <span class="mark"></span>
    <span class="name">Maplewood Family Learning Center</span>
  </div>
  <div class="front-photo" role="img" aria-label="Photo of smiling children in school uniforms flexing their arms in front of a red brick wall"></div>
  <p class="front-tagline">Educational and community-building programs<br>for children, youth and families.</p>
  <div class="donate-box">
    <div class="small">To contribute, please visit</div>
    <div class="url">www.maplewood-kids.org</div>
    <div class="small">and click on the Donate button</div>
  </div>
  <footer class="front-footer">
    <span>412 N. Alder Ave Brookdale, CA 90000</span>
    <span class="social">Find us online – search Maplewood Family Learning Center <span class="social-square"></span></span>
  </footer>
</section>

<section class="card back">
  <div class="appeal">
    <h2 class="appeal-header">Help Us To Finish Our Year STRONG!</h2>
    <div class="appeal-photo" role="img" aria-label="Photo of children giving each other a high five in a classroom"></div>
    <div class="appeal-body">
      <p class="appeal-copy">Maplewood Family Learning Center is in the middle of its 23rd year of ministry and we need your help to finish our year strong! We need another $40,000 from our individual donors to help end the year in the black. Please help us continue to impact lives through our high quality faith-based educational programs. We serve around 130 children at our four sites in Brookdale, offering a safe and enriching place for children to grow and for families to come together.</p>
      <div class="appeal-cta">To contribute, please visit <b>www.maplewood-kids.org</b><br>and click on the <strong>Donate</strong> button</div>
    </div>
    <address class="appeal-footer">
      412 N. Alder Ave Brookdale, CA 90000<br>
      (555) 014-2281<br>
      hello@maplewoodkids.org
      <span class="social-square"></span>
    </address>
  </div>

  <div class="mailing">
    <address class="return-address">MAPLEWOOD<br>FAMILY LEARNING CENTER<br>412 N. Alder Ave<br>Brookdale, CA 90000</address>
    <div class="stamp-box"></div>
    <div class="address-lines"><span></span><span></span><span></span><span></span><span></span></div>
    <div class="seal">
      <span class="mark"></span>
      <span class="name">Maplewood Family Learning Center</span>
    </div>
    <p class="legal">Maplewood Family Learning Center is a registered 501(c)3<br>nonprofit organization. All donations are tax deductible.<br>Federal Tax ID # 12-3456789</p>
    <div class="mailing-footer">www.maplewood-kids.org</div>
  </div>
</section>

</body>
</html>
```